ALL TEXT Social Media Graphics

We are looking for a series of social media graphics for Instagram (new size: 4:5 (1080 x 1350 pixels) ratio that are ALL TEXT. We want the following quotes below on each graphic; one quote per graphic. AND, In very small letters at the bottom of each graphic, add @PaulaWrenLive
The look and feel of these graphics should be complimentary to the color palette attached below; but keep them simple. But the design is up to you; at the end of this document, I provided various samples of all text graphics that I like as examples.
The Quotes are in the attached WORD document
women trying to lose weight

```html
<!DOCTYPE html>
<html lang="en">
<head>
<meta charset="utf-8">
<title>Summer Slimdown Quote Graphics</title>
<link rel="stylesheet" href="https://fonts.googleapis.com/css2?family=Anton&family=Fira+Sans:wght@300;400&family=Roboto:ital,wght@1,300&family=PT+Sans&display=swap">
<style>
  :root {
    --berry: #a8124f;
    --berry-band: #ad1457;
    --pink-text: #e94a86;
    --rose-band: #f291b3;
    --hot-band: #ee5b8c;
    --blush-band: #fcc3e0;
    --icon-pink: #f6a9c6;
    --paper: #ffffff;
  }
  * { box-sizing: border-box; margin: 0; padding: 0; }
  html, body { width: 1200px; height: 665px; overflow: hidden; background: var(--paper); }
  .canvas { position: relative; width: 1200px; height: 665px; }
  .quote-card {
    position: absolute;
    width: 203px;
    height: 253px;
    background: var(--paper);
    box-shadow: 3px 3px 5px rgba(0,0,0,.35);
    overflow: hidden;
  }
  .headline, .body-copy, .cta { position: absolute; left: 22px; right: 6px; }
  .headline {
    font-family: "Anton", "Impact", sans-serif;
    color: var(--berry);
    font-size: 17.5px;
    line-height: 21.5px;
    letter-spacing: -0.2px;
  }
  .body-copy {
    font-family: "Fira Sans", sans-serif;
    font-weight: 300;
    color: var(--pink-text);
    font-size: 12.5px;
    line-height: 16px;
    letter-spacing: 0.3px;
  }
  .cta {
    font-family: "Roboto", sans-serif;
    font-style: italic;
    font-weight: 300;
    color: var(--pink-text);
    font-size: 13px;
    line-height: 16px;
  }
  .waist-figure, .apple-badge { position: absolute; }
  .waist-figure {
    width: 32px; height: 30px;
    border-radius: 8px 8px 10px 10px;
    background: linear-gradient(180deg, var(--icon-pink) 0%, #fbe3ee 55%, var(--berry) 100%);
  }
  .apple-badge {
    width: 38px; height: 38px;
    border-radius: 50%;
    border: 1.2px solid var(--icon-pink);
    background: radial-gradient(circle, #fde8f1 0%, #ffffff 70%);
  }
  .handle-band {
    position: absolute; left: 0; right: 0; bottom: 0;
    height: 26px;
    display: flex; align-items: center; justify-content: center;
    font-family: "PT Sans", sans-serif;
    font-size: 10px;
    color: var(--paper);
  }
  .band-berry { background: var(--berry-band); }
  .band-rose { background: var(--rose-band); }
  .band-hot { background: var(--hot-band); }
  .band-blush { background: var(--blush-band); }
</style>
</head>
<body>
<main class="canvas">

  <section class="quote-card" style="left:54px;top:75px">
    <h2 class="headline" style="top:18px">You can absolutely<br>be down 20–30<br>pounds</h2>
    <p class="body-copy" style="top:92px">by end of summer.<br>All it takes is<br>the right plan—<br>and you’ve found it.</p>
    <div class="waist-figure" style="left:136px;top:113px" role="img" aria-label="Small waist figure icon"></div>
    <p class="cta" style="top:168px">Comment “Glow Girl ”<br>for the Glow Girl<br>Summer Slimdown!</p>
    <footer class="handle-band band-berry">@PaulaWrenLive</footer>
  </section>

  <section class="quote-card" style="left:280px;top:75px">
    <h2 class="headline" style="top:18px">You don’t need another<br>diet—you need a<br>system that works.</h2>
    <p class="body-copy" style="top:104px">Drop 30 pounds with the<br>Glow Girl Summer<br>Slimdown.</p>
    <div class="apple-badge" style="left:135px;top:130px" role="img" aria-label="Apple icon in a circle"></div>
    <p class="cta" style="top:166px">Comment “Summer”<br>to start now</p>
    <footer class="handle-band band-rose">@PaulaWrenLive</footer>
  </section>

  <section class="quote-card" style="left:509px;top:75px">
    <h2 class="headline" style="top:25px">There’s still time to<br>drop the 30 pounds and<br>slay this summer.</h2>
    <p class="body-copy" style="top:106px">The Glow Girl Summer<br>Slimdown has the<br>blueprint.</p>
    <div class="waist-figure" style="left:148px;top:130px" role="img" aria-label="Small waist figure icon"></div>
    <p class="cta" style="top:170px">Comment “Glow Girl”!</p>
    <footer class="handle-band band-berry">@PaulaWrenLive</footer>
  </section>

  <section class="quote-card" style="left:732px;top:75px">
    <h2 class="headline" style="top:18px">Nothing feels better than<br>seeing that scale drop<br>week after week.</h2>
    <p class="body-copy" style="top:96px">Let’s lose up to<br>30 pounds this summer<br>—together.</p>
    <div class="apple-badge" style="left:143px;top:143px" role="img" aria-label="Apple icon in a circle"></div>
    <p class="cta" style="top:160px">Comment “Summer”<br>to join the Glow<br>Girl Summer Slimdown!</p>
    <footer class="handle-band band-rose">@PaulaWrenLive</footer>
  </section>

  <section class="quote-card" style="left:960px;top:73px">
    <h2 class="headline" style="top:25px">Don’t wait ‘til next<br>summer to get right.<br>The time is NOW.</h2>
    <p class="body-copy" style="top:110px">Drop 30 pounds with<br>the Glow Girl Summer<br>Slimdown.</p>
    <div class="waist-figure" style="left:147px;top:140px" role="img" aria-label="Small waist figure icon"></div>
    <p class="cta" style="top:176px">Comment “Summer”!</p>
    <footer class="handle-band band-berry">@PaulaWrenLive</footer>
  </section>

  <section class="quote-card" style="left:54px;top:341px">
    <h2 class="headline" style="top:18px">This summer ain’t<br>over—and neither are<br>your body goals.</h2>
    <p class="body-copy" style="top:98px">Drop 30 pounds with the<br>Glow Girl Summer<br>Slimdown.</p>
    <div class="waist-figure" style="left:139px;top:126px" role="img" aria-label="Small waist figure icon"></div>
    <p class="cta" style="top:163px">Comment “Glow Girl”<br>to get the plan</p>
    <footer class="handle-band band-hot">@PaulaWrenLive</footer>
  </section>

  <section class="quote-card" style="left:280px;top:341px">
    <h2 class="headline" style="top:30px;left:23px">If your goal is a tiny<br>waist, flat belly,</h2>
    <p class="body-copy" style="top:88px;left:23px">and 30 pounds down—<br>this is the plan.</p>
    <div class="apple-badge" style="left:148px;top:142px" role="img" aria-label="Apple icon in a circle"></div>
    <p class="cta" style="top:136px;left:23px">Comment “Summer”<br>to join the Glow Girl<br>Summer Slimdown!</p>
    <footer class="handle-band band-blush">@PaulaWrenLive</footer>
  </section>

  <section class="quote-card" style="left:509px;top:341px">
    <h2 class="headline" style="top:18px;left:21px">Snatched waist,<br>flat tummy,<br>30 pounds lighter —</h2>
    <p class="body-copy" style="top:103px;left:21px">that’s what the Glow Girl<br>Summer Slimdown<br>Challenge delivers.</p>
    <div class="waist-figure" style="left:149px;top:146px" role="img" aria-label="Small waist figure icon"></div>
    <p class="cta" style="top:173px;left:21px;line-height:21px">Comment “Glow Girl”<br>to get the plan</p>
    <footer class="handle-band band-hot">@PaulaWrenLive</footer>
  </section>

  <section class="quote-card" style="left:737px;top:341px">
    <h2 class="headline" style="top:29px;left:16px">Sis, we’re dropping belly<br>flat and saying goodbye<br>to stubborn pounds.</h2>
    <p class="body-copy" style="top:108px;left:17px">Join the Glow Girl<br>Summer Slimdown—</p>
    <div class="apple-badge" style="left:149px;top:122px" role="img" aria-label="Apple icon in a circle"></div>
    <p class="cta" style="top:163px;left:17px">comment “Summer”!</p>
    <footer class="handle-band band-blush">@PaulaWrenLive</footer>
  </section>

  <section class="quote-card" style="left:960px;top:339px">
    <h2 class="headline" style="top:16px;left:21px">You’ve got 8 weeks<br>and the perfect plan<br>to drop 30 pounds.</h2>
    <p class="body-copy" style="top:96px;left:21px">Let’s get snatched this<br>summer with the<br>Glow Girl Summer<br>Slimdown.</p>
    <div class="waist-figure" style="left:136px;top:134px" role="img" aria-label="Small waist figure icon"></div>
    <p class="cta" style="top:183px;left:24px">Comment “Summer”!</p>
    <footer class="handle-band band-hot">@PaulaWrenLive</footer>
  </section>

</main>
</body>
</html>
```